Business card including two companies and social media

We have two companies, First is TVO Risk Management which provides Insurance products for commercial businesses and second is TVO Financial which provides life, benefits and financial products for our business client owners.. We want to role these two companies into one logo with one business card. We have always seperated the two companies however as we work out the same office and work together to sell the products we would like to re-launch the company as LVQ. We have also implemented a social media page on Facebook, Twitter, Linked in.
www.tvo-example.ca is our web page. This will explain what we are and what we do.

Industry/Entity Type

Business

```html
<!DOCTYPE html>
<html lang="en">
<head>
<meta charset="utf-8">
<title>LVQ Business Card Designs</title>
<link rel="stylesheet" href="https://fonts.googleapis.com/css2?family=Cabin:wght@700&family=Orbitron:wght@400;600&display=swap">
<style>
  :root {
    --board-dark: #2b2b2b;
    --board-mid: #3d3d3d;
    --title: #ffffff;
    --card-black: #231f20;
    --card-white: #ffffff;
    --card-grey: #5f5f5f;
    --card-green: #8dc63f;
    --brand-green: #8dc63f;
    --mark-silver: #d9d9d9;
    --text-light: #f2f2f2;
    --faint-on-grey: rgba(120,120,120,0.55);
    --faint-on-green: rgba(255,255,255,0.16);
    --social-grey: #8a8a8a;
    --social-blue: #3b7fc4;
  }
  * { box-sizing: border-box; margin: 0; padding: 0; }
  html, body { width: 1200px; height: 900px; overflow: hidden; }
  body {
    background: linear-gradient(180deg, var(--board-mid), var(--board-dark));
    position: relative;
    font-family: "Orbitron", sans-serif;
  }
  .board-title {
    position: absolute; top: 24px; left: 0; width: 1125px;
    text-align: center;
    font-family: "Cabin", sans-serif; font-weight: 700;
    font-size: 44px; letter-spacing: 1px; color: var(--title);
  }
  .card {
    position: absolute; overflow: hidden; border-radius: 28px;
    box-shadow: 0 4px 14px rgba(0,0,0,0.35);
  }
  .card--front-black { left: 42px; top: 105px; width: 510px; height: 290px; background: var(--card-black); }
  .card--front-white { left: 645px; top: 100px; width: 520px; height: 293px; background: var(--card-white); }
  .card--back-grey { left: 30px; top: 420px; width: 532px; height: 300px; background: var(--card-grey); }
  .card--back-green { left: 645px; top: 420px; width: 525px; height: 297px; background: var(--card-green); }

  .front-mark {
    position: absolute; inset: 0;
    display: flex; align-items: center; justify-content: center; gap: 18px;
  }
  .front-mark__dot { width: 34px; height: 34px; border-radius: 50%; background: var(--mark-silver); }
  .front-mark__name {
    font-weight: 600; font-size: 64px; letter-spacing: 4px; color: var(--brand-green);
  }

  .back-ring {
    position: absolute; right: -150px; top: -40px;
    width: 360px; height: 360px; border-radius: 50%;
  }
  .card--back-grey .back-ring { background: rgba(110,110,110,0.5); }
  .card--back-green .back-ring { background: var(--faint-on-green); }
  .back-faint-name {
    position: absolute; right: -40px; top: 100px;
    font-weight: 600; font-size: 64px; letter-spacing: 4px; color: var(--faint-on-grey);
  }

  .back-badge {
    position: absolute; left: 25px; top: 218px;
    width: 62px; display: flex; flex-direction: column; align-items: center; gap: 4px;
  }
  .back-badge__dot { width: 40px; height: 40px; border-radius: 50%; background: var(--mark-silver); }
  .back-badge__name { font-weight: 600; font-size: 12px; letter-spacing: 1px; color: var(--brand-green); }
  .card--back-green .back-badge__name { color: #ffffff; }

  .contact {
    position: absolute; left: 115px; top: 202px; height: 88px;
    border-left: 3px solid var(--text-light); padding-left: 12px;
    color: var(--text-light); font-size: 11px; letter-spacing: 1.5px; line-height: 16px;
  }
  .contact__name { font-size: 12px; margin-bottom: 4px; }
  .contact__row { display: flex; align-items: center; gap: 6px; }
  .contact__row svg { width: 10px; height: 10px; flex: none; }
  .social { display: flex; gap: 8px; margin-top: 8px; }
  .social__tile { width: 16px; height: 16px; border-radius: 2px; background: var(--social-grey); }
  .card--back-green .social__tile { background: var(--social-blue); }
</style>
</head>
<body>
  <h1 class="board-title">BUSINESS CARD DESIGNS</h1>

  <section class="card card--front-black" aria-label="Card front, black">
    <div class="front-mark">
      <span class="front-mark__dot"></span>
      <span class="front-mark__name">LVQ</span>
    </div>
  </section>

  <section class="card card--front-white" aria-label="Card front, white">
    <div class="front-mark">
      <span class="front-mark__dot"></span>
      <span class="front-mark__name">LVQ</span>
    </div>
  </section>

  <section class="card card--back-grey" aria-label="Card back, grey">
    <div class="back-ring"></div>
    <div class="back-faint-name">LVQ</div>
    <div class="back-badge">
      <span class="back-badge__dot"></span>
      <span class="back-badge__name">LVQ</span>
    </div>
    <div class="contact">
      <p class="contact__name">YOUR NAME HERE</p>
      <p class="contact__row"><svg viewBox="0 0 10 10"><rect x="2.5" y="0" width="5" height="10" rx="1" fill="currentColor"/></svg>0199 456 789</p>
      <p class="contact__row"><svg viewBox="0 0 10 10"><rect x="0" y="2" width="10" height="6" fill="currentColor"/></svg>NAME@EMAIL.COM</p>
      <p class="contact__row"><svg viewBox="0 0 10 10"><circle cx="5" cy="5" r="4" fill="none" stroke="currentColor" stroke-width="1.5"/></svg>WWW.LVQ-EXAMPLE.COM</p>
      <div class="social" role="img" aria-label="Social media pages">
        <span class="social__tile"></span><span class="social__tile"></span><span class="social__tile"></span>
      </div>
    </div>
  </section>

  <section class="card card--back-green" aria-label="Card back, green">
    <div class="back-ring"></div>
    <div class="back-badge">
      <span class="back-badge__dot"></span>
      <span class="back-badge__name">LVQ</span>
    </div>
    <div class="contact">
      <p class="contact__name">YOUR NAME HERE</p>
      <p class="contact__row"><svg viewBox="0 0 10 10"><rect x="2.5" y="0" width="5" height="10" rx="1" fill="currentColor"/></svg>0199 456 789</p>
      <p class="contact__row"><svg viewBox="0 0 10 10"><rect x="0" y="2" width="10" height="6" fill="currentColor"/></svg>NAME@EMAIL.COM</p>
      <p class="contact__row"><svg viewBox="0 0 10 10"><circle cx="5" cy="5" r="4" fill="none" stroke="currentColor" stroke-width="1.5"/></svg>WWW.LVQ-EXAMPLE.COM</p>
      <div class="social" role="img" aria-label="Social media pages">
        <span class="social__tile"></span><span class="social__tile"></span><span class="social__tile"></span>
      </div>
    </div>
  </section>
</body>
</html>
```